Family Psychologist Needs a Sign Designed - Logo Supplied

I am looking for signage on the front window that is bright and catches people’s eyes as they drive past. Therefore, the writing can’t be too small that it is too hard to focus on and read from a moving car.

I want to maybe incorporate the floating spots somehow. I am also looking to hang a banner over the side of the front railing that lists what services are offered since the name doesn’t exactly cover it all . Services include: Psychology, Speech, OT. There is also an education component to the business where we do Study Skills Coaching to high school kids. I would like to see an option of this incorporated to but in a separate way so it isn’t associated with the “psychology” part of the business as this may deter people.

I also want to put a sign above the business in the overhead light thing (not sure what its called). Currently it is empty but the clinics next door have “chiropractor” and “medical centre” written in theirs so mine will have to be as equally simple but specific. Logo attached (EPS)

Ive also attached my logo and a few examples of where the signagewill go.

```html
<!DOCTYPE html>
<html lang="en">
<head>
<meta charset="utf-8">
<title>Step By Step – Signage Set</title>
<link rel="stylesheet" href="https://fonts.googleapis.com/css2?family=Source+Sans+3:wght@600;700;800&display=swap">
<style>
  :root {
    --teal: #1db598;
    --aqua: #27b9c9;
    --lime: #7dc242;
    --blue: #1e6fb8;
    --brand: #2aa9a6;
    --mark: #3fb39a;
    --ink: #111111;
    --sign-bg: #ffffff;
    --sign-edge: #2a2a2a;
    --bg-light: #ffffff;
    --bg-edge: #dcdcdc;
  }
  * { margin: 0; padding: 0; box-sizing: border-box; }
  html, body { width: 1200px; height: 1000px; overflow: hidden; }
  body {
    position: relative;
    font-family: "Source Sans 3", "Helvetica Neue", Arial, sans-serif;
    background: radial-gradient(ellipse 75% 80% at 58% 45%, var(--bg-light) 0%, #f4f4f4 55%, var(--bg-edge) 100%);
    color: var(--ink);
  }
  .board-label {
    position: absolute;
    font-weight: 700;
    font-size: 23px;
    line-height: 1;
    color: var(--ink);
  }
  .sign {
    position: absolute;
    background: var(--sign-bg);
    border: 1px solid var(--sign-edge);
    box-shadow: 5px 5px 7px rgba(0,0,0,.35);
  }
  .brand-square {
    position: absolute;
    background: var(--mark);
  }
  .brand-name {
    position: absolute;
    font-weight: 800;
    color: var(--brand);
    line-height: 1;
    white-space: nowrap;
  }
  .tagline {
    position: absolute;
    font-weight: 700;
    color: var(--blue);
    line-height: 1;
    white-space: nowrap;
  }

  /* Light box */
  .lightbox { left: 91px; top: 63px; width: 717px; height: 143px; }
  .lightbox .brand-square { left: 22px; top: 37px; width: 85px; height: 85px; }
  .lightbox .brand-name { left: 126px; top: 10px; font-size: 80px; letter-spacing: 2px; }
  .lightbox .tagline { left: 128px; top: 84px; font-size: 46px; letter-spacing: 1px; }

  /* Door signs */
  .door-logo { left: 106px; top: 254px; width: 230px; height: 190px; }
  .door-logo .brand-square { left: 22px; top: 55px; width: 84px; height: 84px; }
  .door-logo .brand-name { left: 111px; top: 62px; font-size: 25px; line-height: .94; }
  .door-logo .tagline { left: 111px; top: 132px; font-size: 10px; }

  .door-services {
    left: 435px; top: 256px; width: 229px; height: 191px;
    display: flex; flex-direction: column; align-items: center; justify-content: center;
    gap: 4px;
  }
  .service-list { list-style: none; text-align: center; font-weight: 600; }
  .door-services .service-list li { font-size: 27px; line-height: 34px; }
  .c-teal { color: var(--teal); }
  .c-aqua { color: var(--aqua); }
  .c-lime { color: var(--lime); }

  /* Window sticker */
  .window { left: 99px; top: 505px; width: 740px; height: 460px; }
  .window .brand-square { left: 76px; top: 105px; width: 272px; height: 268px; }
  .window .brand-name { left: 355px; top: 132px; font-size: 78px; line-height: 70px; letter-spacing: 2px; }
  .window .tagline { left: 355px; top: 350px; font-size: 31px; }
  .window .service-line {
    position: absolute; left: 0; right: 0; top: 395px;
    text-align: center; font-weight: 600; font-size: 28px; white-space: nowrap;
  }
</style>
</head>
<body>
  <h2 class="board-label" style="left:100px; top:22px;">Light Box sign</h2>
  <section class="sign lightbox">
    <span class="brand-square" aria-hidden="true"></span>
    <div class="brand-name">STEP BY STEP</div>
    <div class="tagline">Psychology’s Education</div>
  </section>

  <h2 class="board-label" style="left:112px; top:222px;">door signs</h2>
  <section class="sign door-logo">
    <span class="brand-square" aria-hidden="true"></span>
    <div class="brand-name">STEP<br>BY<br>STEP</div>
    <div class="tagline">Psychology &amp; Education</div>
  </section>
  <section class="sign door-services">
    <ul class="service-list">
      <li class="c-teal">- Psychology -</li>
      <li class="c-aqua">- Speech -</li>
      <li class="c-lime">- OT -</li>
      <li class="c-aqua">- Study Skills -</li>
      <li class="c-aqua">Coaching</li>
    </ul>
  </section>

  <h2 class="board-label" style="left:110px; top:471px;">window sticker</h2>
  <section class="sign window">
    <span class="brand-square" aria-hidden="true"></span>
    <div class="brand-name">STEP<br>BY<br>STEP</div>
    <div class="tagline">Psychology &amp; Education</div>
    <p class="service-line">
      <span class="c-teal">- Psychology</span>
      <span class="c-aqua">- Speech -</span>
      <span class="c-lime">OT</span>
      <span class="c-aqua">- Study Skills Coaching -</span>
    </p>
  </section>
</body>
</html>
```